Personal Trainer and Corporate Health Business

I need a business card for a new company I'm starting in Australia called "Brisk Vitality Partners" I will be providing a Personal training service as well as corporate health in companies.
The service provided is to help promote an active and healthy lifstyle.
The design should communicate a healthy lifestyle and also the benefits that this can have on a personal level and in the corporate environment and the benefits that flow from that.

Target Market(s)

Members of the public and Corporate

Industry/Entity Type

Environment

Requirements
Must have
• Company logo attached
Look and feel fresh and modern

Tag line: "Moving Every Body Toward Better Living"

Lewis Norgate
Managing Director

m: 0417 596 304
e: lewis@briskvitalitypartners.com.au

www.briskvitalitypartners.com.au
Nice to have
• Can be 1 or 2 sided

```html
<!DOCTYPE html>
<html lang="en">
<head>
<meta charset="utf-8">
<title>Brisk Vitality Partners – Business Card</title>
<link href="https://fonts.googleapis.com/css2?family=Mulish:wght@400;600;800&family=Questrial&display=swap" rel="stylesheet">
<style>
  :root {
    --navy: #1f2d6e;
    --navy-deep: #18235a;
    --green: #6cb33f;
    --paper: #f6f6f3;
    --white: #ffffff;
    --backdrop: #2a2d33;
    --font-brand: "Mulish", sans-serif;
    --font-body: "Questrial", sans-serif;
  }
  * { box-sizing: border-box; margin: 0; padding: 0; }
  html, body {
    width: 1200px;
    height: 800px;
    overflow: hidden;
  }
  body {
    background: var(--backdrop);
    font-family: var(--font-body);
    display: flex;
    align-items: center;
    justify-content: center;
    gap: 40px;
  }
  .card {
    width: 540px;
    height: 310px;
    position: relative;
    overflow: hidden;
    border-radius: 3px;
    box-shadow: 0 10px 30px rgba(0,0,0,0.35);
  }

  /* Front */
  .card-front { background: var(--navy); }
  .front-top {
    position: absolute;
    left: 0; top: 0; right: 0;
    height: 150px;
    background: var(--paper);
    border-bottom: 6px solid var(--green);
    display: flex;
    align-items: center;
    justify-content: center;
    gap: 14px;
  }
  .brand-dot {
    width: 22px;
    height: 22px;
    border-radius: 50%;
    background: var(--green);
    flex: none;
  }
  .brand-name {
    font-family: var(--font-brand);
    color: var(--navy);
    font-weight: 600;
    font-size: 30px;
    letter-spacing: 0.5px;
    white-space: nowrap;
  }
  .holder {
    position: absolute;
    left: 36px;
    top: 206px;
  }
  .holder-name {
    font-family: var(--font-brand);
    color: var(--white);
    font-weight: 800;
    font-size: 18px;
    letter-spacing: 0.5px;
    text-transform: uppercase;
  }
  .holder-role {
    color: var(--green);
    font-size: 15px;
    margin-top: 4px;
  }
  .contacts {
    position: absolute;
    left: 238px;
    top: 180px;
    list-style: none;
    display: flex;
    flex-direction: column;
    gap: 9px;
  }
  .contact {
    display: flex;
    align-items: center;
    gap: 9px;
    color: var(--white);
    font-size: 14px;
    white-space: nowrap;
  }
  .contact svg { width: 18px; height: 18px; flex: none; }

  /* Back */
  .card-back {
    background: linear-gradient(160deg, var(--navy) 0%, var(--navy-deep) 100%);
    display: flex;
    flex-direction: column;
    align-items: center;
    justify-content: center;
    gap: 26px;
  }
  .back-brand {
    display: flex;
    align-items: center;
    gap: 14px;
  }
  .back-brand .brand-name { color: var(--white); }
  .tagline {
    color: var(--white);
    font-size: 16px;
    letter-spacing: 0.3px;
  }
</style>
</head>
<body>

  <section class="card card-front">
    <div class="front-top">
      <span class="brand-dot"></span>
      <span class="brand-name">Brisk Vitality Partners</span>
    </div>

    <div class="holder">
      <p class="holder-name">Lewis Norgate</p>
      <p class="holder-role">Managing Director</p>
    </div>

    <ul class="contacts">
      <li class="contact">
        <svg viewBox="0 0 18 18" aria-hidden="true">
          <circle cx="9" cy="9" r="8" fill="none" stroke="#6cb33f" stroke-width="1.3"/>
          <rect x="6.3" y="4" width="5.4" height="10" rx="1" fill="none" stroke="#6cb33f" stroke-width="1.2"/>
          <line x1="8" y1="12.3" x2="10" y2="12.3" stroke="#6cb33f" stroke-width="1"/>
        </svg>
        0417 596 304
      </li>
      <li class="contact">
        <svg viewBox="0 0 18 18" aria-hidden="true">
          <circle cx="9" cy="9" r="8" fill="none" stroke="#6cb33f" stroke-width="1.3"/>
          <rect x="4.5" y="6" width="9" height="6.2" fill="none" stroke="#6cb33f" stroke-width="1.2"/>
          <polyline points="4.5,6 9,9.6 13.5,6" fill="none" stroke="#6cb33f" stroke-width="1.2"/>
        </svg>
        lewis@briskvitalitypartners.com.au
      </li>
      <li class="contact">
        <svg viewBox="0 0 18 18" aria-hidden="true">
          <circle cx="9" cy="9" r="8" fill="none" stroke="#6cb33f" stroke-width="1.3"/>
          <circle cx="9" cy="9" r="4.8" fill="none" stroke="#6cb33f" stroke-width="1"/>
          <ellipse cx="9" cy="9" rx="2" ry="4.8" fill="none" stroke="#6cb33f" stroke-width="1"/>
          <line x1="4.2" y1="9" x2="13.8" y2="9" stroke="#6cb33f" stroke-width="1"/>
        </svg>
        www.briskvitalitypartners.com.au
      </li>
    </ul>
  </section>

  <section class="card card-back">
    <div class="back-brand">
      <span class="brand-dot"></span>
      <span class="brand-name">Brisk Vitality Partners</span>
    </div>
    <p class="tagline">Moving Every Body Toward Better Living</p>
  </section>

</body>
</html>
```